Computer tuition business needs Business card and Advertising Flyer

I am starting up a new business "Dorian Featherby Computer Services" (DFCS for short) based in the Kestrel Valley Southland Coast.
The primary focus is on tuition\advice to the elderly and less computer literate in the region.
I will not be providing any repair services.

I have the line "At your home, On your computer, Answering your questions" in my head

I will need a Business card design (one sided) and Advertising Flyer design (A4 size, grayscale ).

Contact details on all these are - Mobile: 0412-683-904
- Email : dfeatherby.techhelp@examplemail.net

Target Market(s)

The primary focus is on tuition\advice to the elderly and less computer literate in the Manning Valley region of

Industry/Entity Type

Computer

```html
<!DOCTYPE html>
<html lang="en">
<head>
<meta charset="utf-8">
<title>Dorian Featherby Computer Services – Business Card</title>
<link rel="stylesheet" href="https://fonts.googleapis.com/css2?family=Didact+Gothic&display=swap">
<style>
  :root {
    --frame-grey: #6e6e6e;
    --paper-light: #f4f4f4;
    --paper-mid: #dcdcdc;
    --ink-dark: #2f2f2f;
    --accent-blue: #3fa3cc;
    --panel-blue-light: #5fb2d2;
    --panel-blue-dark: #3d93b6;
    --white: #ffffff;
  }
  * { box-sizing: border-box; margin: 0; padding: 0; }
  html, body { width: 720px; height: 1200px; overflow: hidden; background: var(--frame-grey); }
  body { font-family: "Didact Gothic", "Helvetica Neue", Arial, sans-serif; }

  .card {
    position: relative;
    width: 720px;
    height: 1200px;
    background: var(--frame-grey);
  }
  .card-face {
    position: absolute;
    left: 34px; top: 34px;
    width: 652px; height: 1132px;
    background: linear-gradient(135deg, var(--paper-light) 0%, var(--paper-mid) 45%, var(--paper-light) 70%, var(--paper-mid) 100%);
  }
  .brand-initials {
    position: absolute;
    left: 0; top: 200px;
    width: 720px;
    text-align: center;
    color: var(--ink-dark);
    font-size: 110px;
    line-height: 120px;
    letter-spacing: 6px;
    font-weight: 400;
  }
  .brand-name {
    position: absolute;
    left: 0; top: 462px;
    width: 720px;
    text-align: center;
    font-size: 56px;
    line-height: 64px;
    letter-spacing: 1px;
    text-transform: uppercase;
    font-weight: 400;
  }
  .brand-name .name-line { display: block; color: var(--ink-dark); }
  .brand-name .trade-line { display: block; color: var(--accent-blue); }
  .contact-panel {
    position: absolute;
    left: 106px; top: 640px;
    width: 558px; height: 470px;
    border-top-left-radius: 34px;
    border-top-right-radius: 10px;
    background: linear-gradient(160deg, var(--panel-blue-light) 0%, var(--panel-blue-dark) 100%);
  }
  .contact-row {
    position: absolute;
    left: 113px;
    display: flex;
    align-items: center;
    width: 551px;
  }
  .contact-icon {
    width: 80px; height: 80px;
    background: var(--white);
    border-radius: 6px;
    display: flex; align-items: center; justify-content: center;
    flex: none;
  }
  .contact-icon svg { width: 42px; height: 42px; fill: var(--ink-dark); }
  .contact-text {
    color: var(--white);
    font-size: 32px;
    line-height: 40px;
    white-space: nowrap;
  }
  .row-email { top: 700px; }
  .row-email .contact-text { font-size: 21px; margin-left: 18px; }
  .row-phone { top: 855px; }
  .row-phone .contact-text { margin-left: 72px; letter-spacing: 1px; }
  .row-location { top: 1000px; }
  .row-location .contact-text { width: 450px; text-align: center; line-height: 38px; }
</style>
</head>
<body>
  <main class="card">
    <div class="card-face" role="img" aria-label="Light grey geometric low-poly background texture"></div>

    <div class="brand-initials">DFCS</div>
    <h1 class="brand-name"><span class="name-line">Dorian Featherby</span><span class="trade-line">Computer Services</span></h1>

    <div class="contact-panel" role="img" aria-label="Blue panel with subtle hexagon texture"></div>

    <div class="contact-row row-email">
      <span class="contact-icon">
        <svg viewBox="0 0 24 24" aria-hidden="true"><path d="M4 5h16v10H4z M6 7v6h12V7z M2 17h20v2H2z" fill-rule="evenodd"/></svg>
      </span>
      <span class="contact-text">dfeatherby.techhelp@examplemail.net</span>
    </div>

    <div class="contact-row row-phone">
      <span class="contact-icon">
        <svg viewBox="0 0 24 24" aria-hidden="true"><path d="M6.6 10.8a15.2 15.2 0 0 0 6.6 6.6l2.2-2.2a1 1 0 0 1 1-.25 11.4 11.4 0 0 0 3.6.57 1 1 0 0 1 1 1V20a1 1 0 0 1-1 1A17 17 0 0 1 3 4a1 1 0 0 1 1-1h3.5a1 1 0 0 1 1 1c0 1.25.2 2.45.57 3.57a1 1 0 0 1-.25 1z"/></svg>
      </span>
      <span class="contact-text">0412-683-904</span>
    </div>

    <div class="contact-row row-location">
      <span class="contact-icon">
        <svg viewBox="0 0 24 24" aria-hidden="true"><path d="M12 2a7 7 0 0 0-7 7c0 5.25 7 13 7 13s7-7.75 7-13a7 7 0 0 0-7-7zm0 9.5A2.5 2.5 0 1 1 12 6.5a2.5 2.5 0 0 1 0 5z"/></svg>
      </span>
      <span class="contact-text">Kestrel Valley<br>Southland Coast</span>
    </div>
  </main>
</body>
</html>
```